MallPoint Brochure/Booklet Design

I am seeking a luxury finish booklet with the attached content. The same pictures can be used or different ones. It needs to be classy, but EDGY

This new company targets the owners of shopping centres and provides a number of services including marketing/community involvement/digital technology/social media etc. I'd love to see the use of our logo colours and a way to make this really pop!

I'm looking to develop a relationship with a designer that we can work on many more projects with.

I'm not interested in seeing any SAMPLES, only designs that use the brief (our content, logo, colours and font).
Updates

Please do not submit SAMPLES of your other work, we are only interested in seeing designs that work to our brief (content, logo, colour and font)

Reason: There has not been any designs submitted that are of a high enough standard. I'd like to see more use of the colours as backgrounds rather than plain white and some more interesting ideas. Please do not submit samples of your other works.

for brochure inspiration check out the following links... i think bright/classy

Target Market(s)

corporate but with a wow, not standard - this is something millionaires and billionaires will be presented with and they will only look at it for 5 mins so it needs to grab them!

http://www.brelvanto.example/blog/handpicked-printed-brochures/

http://quorvelstudio.example/articles/30-best-brochure-designs-for-your-inspiration/

http://www.tamsifolio.example/2012/04/26/40-unique-and-beautiful-examples-of-brochure-design/

Industry/Entity Type

Shopping

Font styles to use
Other font styles liked:
• ubuntu

Requirements
Must have
• Must have the content supplied included and our logo used
Must use UBUNTU font
Should not have
• Should not be a sample, must abide by the brief

```html
<!DOCTYPE html>
<html lang="en">
<head>
<meta charset="utf-8">
<title>MallPoint Brochure</title>
<link href="https://fonts.googleapis.com/css2?family=Ubuntu:ital,wght@0,300;0,400;0,500;1,400&display=swap" rel="stylesheet">
<style>
  :root {
    --brand-blue: #1f6bff;
    --text-blue: #2a6ef0;
    --white: #ffffff;
    --ink: #111111;
    --silver-light: #e9e9ec;
    --silver-mid: #c9c9cf;
    --tile-blue: #5cc6ee;
    --tile-pale: #bfe6f6;
  }
  html, body {
    margin: 0;
    padding: 0;
    width: 1200px;
    height: 851px;
    overflow: hidden;
    font-family: "Ubuntu", sans-serif;
  }
  .brochure {
    position: relative;
    width: 1200px;
    height: 851px;
    overflow: hidden;
    background: var(--white);
  }

  /* Front cover */
  .cover {
    position: absolute;
    left: 0; top: 0;
    width: 600px; height: 851px;
    background: var(--brand-blue);
  }
  .cover-mark {
    position: absolute;
    left: 270px; top: 330px;
    width: 60px; height: 60px;
    border-radius: 50%;
    background: var(--white);
  }
  .cover-name {
    position: absolute;
    left: 0; width: 600px;
    top: 494px;
    margin: 0;
    text-align: center;
    color: var(--white);
    font-weight: 500;
    font-size: 88px;
    line-height: 1;
    letter-spacing: -1px;
  }

  /* Inside page */
  .inner {
    position: absolute;
    left: 600px; top: 0;
    width: 495px; height: 851px;
    background: linear-gradient(to bottom, #3d7fff 0px, #7fa8ff 120px, #c9dbff 200px, #eef3ff 240px, #ffffff 262px, #ffffff 100%);
  }
  .headline {
    position: absolute;
    left: 42px; top: 36px;
    margin: 0;
    color: var(--white);
    font-weight: 300;
    text-transform: uppercase;
    white-space: nowrap;
  }
  .headline .lead { display: block; font-size: 58px; line-height: 58px; margin-bottom: 0; }
  .headline .rest { display: block; font-size: 43px; line-height: 46px; }
  .headline em { font-style: italic; font-weight: 400; }

  .shopper-types {
    position: absolute;
    left: 42px; top: 255px;
    margin: 0; padding: 0;
    list-style: none;
    font-size: 14px;
    line-height: 18px;
    color: var(--ink);
    white-space: nowrap;
  }
  .shopper-types li { height: 30px; }
  .shopper-types li::before { content: "•"; color: var(--text-blue); margin-right: 4px; }

  .arrow {
    position: absolute;
    left: 52px; top: 370px;
    width: 90px; height: 100px;
  }

  .services {
    position: absolute;
    left: 42px; top: 492px;
    margin: 0; padding: 0;
    list-style: none;
    color: var(--text-blue);
    font-weight: 300;
    font-size: 19.5px;
    line-height: 21px;
    white-space: nowrap;
  }
  .services li { margin-bottom: 9px; }

  .shopper-figure {
    position: absolute;
    left: 238px; top: 236px;
    width: 225px; height: 275px;
    background: radial-gradient(ellipse at 55% 50%, var(--silver-light) 0%, var(--silver-mid) 50%, rgba(255,255,255,0) 72%);
  }
  .marketing-tiles {
    position: absolute;
    left: 252px; top: 615px;
    width: 220px; height: 215px;
    background: radial-gradient(ellipse at 55% 45%, var(--tile-blue) 0%, var(--tile-pale) 45%, #eeeeee 62%, rgba(255,255,255,0) 72%);
  }

  /* Spine */
  .spine {
    position: absolute;
    left: 1095px; top: 0;
    width: 105px; height: 851px;
    background: var(--brand-blue);
  }
  .spine-name {
    position: absolute;
    left: 55px; top: 200px;
    margin: 0;
    transform: translate(-50%, -50%) rotate(-90deg);
    white-space: nowrap;
    color: var(--white);
    font-weight: 500;
    font-size: 66px;
    line-height: 1;
  }
</style>
</head>
<body>
<main class="brochure">
  <section class="cover">
    <span class="cover-mark" aria-hidden="true"></span>
    <h1 class="cover-name">MallPoint</h1>
  </section>

  <section class="inner">
    <h2 class="headline">
      <span class="lead">We know</span>
      <span class="rest">What customers<br>want when they<br>visit <em>your</em> centre</span>
    </h2>

    <ul class="shopper-types">
      <li>Buzz-activated shoppers</li>
      <li>Autopilot shoppers</li>
      <li>Bargain-activated shoppers</li>
      <li>Variety-activated shoppers</li>
    </ul>

    <svg class="arrow" viewBox="0 0 90 100" aria-hidden="true">
      <path d="M82 4 C40 10 22 32 30 62 L12 58 L48 96 L66 50 L48 58 C42 34 56 16 82 4 Z" fill="var(--brand-blue)"/>
    </svg>

    <ul class="services">
      <li>Grand Openings</li>
      <li>Competitions</li>
      <li>Giveaways</li>
      <li>School holiday<br>activities</li>
      <li>Christmas / Easter /<br>Mother’s Day / Aus Day<br>/ Seasonal / Updatable</li>
      <li>Interactivity</li>
      <li>Management /<br>Promotion of sales</li>
    </ul>

    <div class="shopper-figure" role="img" aria-label="Silver mannequin figure pushing a shopping trolley"></div>
    <div class="marketing-tiles" role="img" aria-label="Letter tiles crossword spelling promotion, product, price and place"></div>
  </section>

  <aside class="spine">
    <p class="spine-name">MallPoint</p>
  </aside>
</main>
</body>
</html>
```